Flyer für eine 24/7 Sicherheitslösung
Vielen, herzlichen Dank! KoRu hat sich sehr schnell und großartig in die Aufgabe zur Gestaltung eines Flyers/Folders für das Empfehlungsmarketing hineingearbeitet. Aus der Anforderungsbeschreibung für einen Flyer mit Rückantwortkarte sowie weiteren Informationen aus dem Briefing wurden selbstständig alle zur Verfügung stehenden Informationskanäle genutzt und in einem tollen Design umgesetzt. Änderungswünsche sind umgehend bearbeitet und mit eigenen Ideen optimiert worden. Toll!!! Meine uneingeschränkte Empfehlung.
Zielgruppe
Ich bin Technischer Berater zu den Themen energienahe Dienstleistungen, Photovoltaik, Stromspeicher, Smart Home und Gefahrenmeldeanlagen für häusliche Gefahren und Einbruch.
Zielgruppe für dieses Projekt sind Eigenheimbesitzer (Haus oder Eigentumswohnung) und kleine Gewerbetreibende, die ein Sicherheitsbedürfnis verspüren, Angst haben und bestenfalls die Vorzüge eines Smart Homes bereits für sich erkannt haben.
Aufgabenstellung
Es soll für das Empfehlungsmarketing ein Flyer zum Thema 24/7 Sicherheitslösung im Smart Home entwickelt werden.
Neben entsprechenden Informationen soll eine postalisch konforme Rückantwort-Karte (Bitte freimachen - falls Marke zur Hand) auf einem vierseitigen Flyer mit Abrisskante für die Rückantwort-Karte entstehen.
Es muss also möglich sein, einmal die Daten des Werbenden und einmal die Daten des Geworbenen mit seiner Unterschrift auf der Karte zu notieren. Die Unterschrift ist aus Verbraucher-/Datenschutzgründen notwendig, damit diese Privatperson somit ihre Erlaubnis erteilt, dass sie von mir kontaktiert werden darf.
Und natürlich müssen sich auch meine Kontaktdaten auf dem Flyer wiederfinden - nur der Vollständigkeit halber. :-)
Ziel ist es einerseits, Verbrauchern den Flyer zur Weitergabe an Freunde, Nachbarn etc. und andererseits den Flyer an Gewerbetreibende zu reichen.
Freundschaftswerbung soll mit je 25 Euro für den Werber und den Geworbenen (Familienmitglieder im gleichen Haushalt ausgeschlossen) bei erfolgreicher Vermittlung, also Zustandekommen eines Auftrags, honoriert werden.
Bei Gewerbetreibende wird jede erfolgreiche Vermittlung, also mit Zustandekommen eines Auftrags, mit 50,00 Euro zzgl. MwSt. honoriert werden. Der Mindestauftragswert soll bei 950,00 Euro (brutto) liegen.
Zur groben Orientierung oder Anregung kann die Website https://schutzsysteme.brelvon.de eingesehen werden.
Die Begrifflichkeiten Sicherheit und Lösung sollen im Vordergrund kommuniziert werden. Die 24/7 Sicherheitslösung bezieht sich auf eine Gefahrenmeldeanlage, vorrangig zur Verhinderung von Schäden aus häuslichen Gefahren wie Rauch, Feuer, Wasser und Gas sowie Einbruch und Diebstahl mit Aufschaltung auf eine Notrufserviceleitstelle. Unter Umständen ist sogar eine staatliche Förderung gegeben.
Es kann auch auf Presse- und Bildmaterial des Herstellers FALKOR-Systemtechnik (http://kurzlnk.de/7QwrtZm) bzw. Pressebilder de Pol..

```html
<!DOCTYPE html>
<html lang="de">
<head>
<meta charset="utf-8">
<title>sicherwerk – 24/7 Sicherheitslösungen</title>
<link rel="stylesheet" href="https://fonts.googleapis.com/css2?family=Jost:wght@300;400&family=Nunito:wght@800;900&display=swap">
<style>
  :root{
    --orange:#ec7d2a;
    --blue-light:#4f80c1;
    --blue-navy:#0e3a86;
    --blue-mid:#2b55a4;
    --white:#ffffff;
    --ink:#1f3f86;
  }
  *{margin:0;padding:0;box-sizing:border-box}
  html,body{width:1200px;height:583px;overflow:hidden;background:#fff}
  body{font-family:'Jost',sans-serif;font-weight:300;color:var(--white)}
  .flyer{position:relative;width:1200px;height:583px;overflow:hidden}
  .panel{position:absolute;top:0;height:583px}
  .panel--left{left:0;width:401px}
  .panel--middle{left:401px;width:399px}
  .panel--right{left:800px;width:400px}
  .photo{position:absolute}
  .strong{font-family:'Nunito',sans-serif;font-weight:900}
  .callout{position:absolute;background:var(--orange);color:var(--white);line-height:1.2}
  .info{position:absolute;left:0;top:291px;height:292px;width:100%}
  .info--left{background:var(--blue-light);padding:17px 20px 0 21px}
  .info--middle{background:var(--blue-navy);padding:17px 20px 0 22px}
  h2{font-family:'Nunito',sans-serif;font-weight:900;font-size:19px;letter-spacing:.2px;margin-bottom:7px}
  .body-copy{font-size:10px;line-height:1.25;margin-bottom:10px}
  .contact-line{font-size:13px;line-height:1.55}
  .contact-line b{font-family:'Nunito',sans-serif;font-weight:900;font-size:12px}
  .brand{position:absolute;font-family:'Nunito',sans-serif;font-weight:800;color:var(--ink);white-space:nowrap;line-height:1}
  .brand--light{color:var(--white)}
  .side-strip{position:absolute;left:800px;top:291px;width:48px;height:147px;background:var(--blue-navy)}
  .side-strip p{position:absolute;left:50%;top:50%;transform:translate(-50%,-50%) rotate(-90deg);white-space:nowrap;font-size:10.5px;line-height:1.15;text-align:center}
  .offers{position:absolute;left:0;top:438px;width:400px;height:145px;background:var(--blue-mid)}
  .offers h3{position:absolute;left:122px;top:21px;font-family:'Nunito',sans-serif;font-weight:900;font-size:13px}
  .offers ul{position:absolute;list-style:none;font-size:13px;line-height:22.5px;white-space:nowrap}
  .imprint{position:absolute;left:22px;top:237px;font-size:10.5px;line-height:1.25}
</style>
</head>
<body>
<div class="flyer">

  <section class="panel panel--left">
    <div class="photo" role="img" aria-label="Foto: Feuer und Flammen im Raum" style="left:0;top:0;width:194px;height:140px;background:linear-gradient(160deg,#7a3a14,#e79a2e 55%,#3a2a22)"></div>
    <div class="photo" role="img" aria-label="Foto: Überwachungskamera an einer Backsteinwand" style="left:194px;top:0;width:207px;height:140px;background:linear-gradient(120deg,#8a3a32,#b65a4a 60%,#6e2e28)"></div>
    <div class="photo" role="img" aria-label="Foto: Wasserrohrbruch mit spritzendem Wasser" style="left:0;top:140px;width:246px;height:151px;background:linear-gradient(90deg,#b64a55,#d9a0a4 60%,#e8e2e0)"></div>
    <div class="photo" role="img" aria-label="Foto: Einbrecher mit Kapuze an einem Fenster" style="left:246px;top:140px;width:155px;height:151px;background:linear-gradient(135deg,#2a2a2c,#4d5048 60%,#8a8a7a)"></div>
    <div class="callout" style="left:0;top:17px;width:227px;height:64px;padding:7px 0 0 16px;font-size:12px">
      Schon ab 1,50 Euro / Tag<br>
      <span class="strong" style="font-size:11.5px">Jetzt kostenfrei beraten lassen<br>und sofort sicher fühlen!</span>
    </div>
    <div class="info info--left">
      <h2>Gefahrenmeldung</h2>
      <p class="body-copy">Unsere sicher | Haus Gefahrenmelder alarmieren zuverlässig bei Hitze, Rauch, Kohlenmonoxid- und Wasseraustritt sowie medizinischen Notfällen.<br>Die Alarmmeldung erfolgt bei der Notrufservice-Leitstelle und Sie werden umgehend auf dem SmartPhone informiert.</p>
      <h2>Einbruchschutz</h2>
      <p class="body-copy" style="margin-bottom:18px">Die sicher | Alarm Einbruchmelder überwachen Zutritts- und Durchgangsbereiche in Wohnung, Haus oder Gewerbebetrieb. Lautstarke Sirenen vergrämen die Eindringlinge. Die Notrufservice-Leitstelle setzt nach Ihren Vorgaben Interventionskräfte ein.</p>
      <p class="contact-line"><b>Immer geöffnet</b> info@sicherwerk.de</p>
      <p class="contact-line"><b>Kostenfreie Beratung</b>&nbsp; Telefon 04512&nbsp; 340 917</p>
      <p class="contact-line"><b>Mo. - Fr.: 9:00 - 17:00 Uhr</b>&nbsp; Sa. - So.: Geschlossen</p>
    </div>
  </section>

  <section class="panel panel--middle">
    <div class="photo" role="img" aria-label="Foto: Familie mit Kind vor dem Eingang eines weißen Hauses" style="left:0;top:0;width:399px;height:291px;background:linear-gradient(100deg,#4e7a34 0%,#9cb67a 18%,#e9eae6 40%,#d9dcdc 70%,#f2f2f0 100%)"></div>
    <div style="position:absolute;right:0;top:214px;width:120px;height:77px;background:#fff;border-top-left-radius:120px 77px"></div>
    <div class="brand" style="right:18px;top:268px;font-size:15px">sicherwerk</div>
    <div class="callout" style="left:0;top:17px;width:196px;height:45px;padding:5px 0 0 18px;font-size:13px">
      24/7 <span class="strong">Sicherheitslösungen</span><br>mit <span class="strong">Funk Alarmanlagen</span>
    </div>
    <div class="info info--middle">
      <h2>Wir sind gern für Sie da!</h2>
      <p class="body-copy" style="margin-top:12px">sicherwerk ist Partner im VIGILIS - Beratungsnetzwerk für kriminaltechnische Prävention.</p>
      <p class="body-copy">Wir planen und installieren maßgeschneiderte Sicherheitslösungen und überwachen diese in einer 24/7 Alarmzentrale mit Veranlassung der im Notfall erforderlichen Maßnahmen.</p>
      <p class="body-copy" style="font-family:'Nunito',sans-serif;font-weight:800">Unseren Kundenservice erreichen Sie von Montag bis Freitag in der Zeit von 09:00 bis 17:00 Uhr.</p>
      <p class="contact-line"><b>Kostenfreie Beratung</b>&nbsp; Telefon 04512&nbsp; 340 917</p>
      <p class="imprint"><b class="strong">sicherwerk</b> | technik und sicherheitsmanagement<br>Lindenweg 7 | D-23619 Hammerstein</p>
      <div class="brand brand--light" style="right:24px;top:237px;font-size:19px">sicherwerk</div>
    </div>
  </section>

  <section class="panel panel--right">
    <div class="brand" style="left:30px;top:42px;font-size:32px">sicherwerk</div>
    <div class="photo" role="img" aria-label="Foto: Einbrecher hebelt ein Fenster mit einem Brecheisen auf" style="left:0;top:118px;width:400px;height:320px;background:linear-gradient(110deg,#1e1e22 0%,#3a3a40 45%,#c9ccd0 62%,#5e7a52 85%,#8aa27a 100%)"></div>
    <div class="callout" style="left:91px;top:118px;width:309px;height:64px;padding:7px 0 0 14px;font-size:19px;line-height:1.2">
      24/7 <span class="strong">Sicherheitslösungen</span><br>für Ihr <span class="strong">Smart Home</span>
    </div>
    <div class="offers">
      <svg style="position:absolute;left:69px;top:14px" width="34" height="34" viewBox="0 0 34 34" fill="none" stroke="#fff" stroke-width="1.6" aria-hidden="true">
        <rect x="1" y="4" width="12" height="12"/><rect x="20" y="2" width="11" height="11" transform="rotate(45 25.5 7.5)"/><rect x="1" y="21" width="12" height="12"/><rect x="19" y="21" width="12" height="12"/>
      </svg>
      <h3>Unsere Angebote</h3>
      <ul style="left:123px;top:45px"><li>sicher | Alarm</li><li>sicher | Pflege</li><li>sicher | Haus</li></ul>
      <ul style="left:236px;top:45px"><li>Sicherheitstechnik</li><li>Altersgerechtes Wohnen</li><li>Hausautomation</li></ul>
    </div>
  </section>

  <div class="side-strip"><p><span class="strong">Kostenfreie Beratung!</span><br>Telefon 04512&nbsp; 340 917</p></div>
</div>
</body>
</html>
```